furniture and home contents restoration

I need to list the services that we perform in our studio.
we serve the general public as well as the insurance/ remediation industry

```html
<!DOCTYPE html>
<html lang="en">
<head>
<meta charset="utf-8">
<title>Hallbrook Studio – Business Card</title>
<link href="https://fonts.googleapis.com/css2?family=Barlow:wght@400;500;700&family=Roboto+Condensed:wght@400;500&display=swap" rel="stylesheet">
<style>
  :root {
    --bg: #4a4b4e;
    --card-dark: #1d1d1e;
    --card-light: #ffffff;
    --ink-light: #f4f4f4;
    --ink-dark: #1a1a1a;
    --rule: #8a8a8a;
  }
  * { margin: 0; padding: 0; box-sizing: border-box; }
  html, body { width: 1200px; height: 801px; overflow: hidden; }
  body {
    background: var(--bg);
    font-family: "Barlow", sans-serif;
    position: relative;
  }
  .card {
    position: absolute;
    top: 240px;
    width: 560px;
    height: 320px;
    background: var(--card-light);
    box-shadow: 0 6px 18px rgba(0,0,0,.35);
    overflow: hidden;
  }
  .card--back { left: 27px; }
  .card--front { left: 613px; }
  .card__dark {
    position: absolute; left: 0; top: 0; width: 100%; height: 214px;
    background: var(--card-dark);
  }
  .card__band {
    position: absolute; left: 0; top: 214px; width: 100%; height: 106px;
    display: flex; flex-direction: column; justify-content: center; align-items: center;
    color: var(--ink-dark); text-align: center;
  }
  .services {
    position: absolute; top: 26px;
    list-style: none;
    font-family: "Roboto Condensed", sans-serif;
    font-size: 11.5px; font-weight: 500;
    color: var(--ink-light);
    line-height: 16.5px;
  }
  .services--left { left: 34px; }
  .services--right { left: 300px; }
  .services li { position: relative; padding-left: 18px; }
  .services li::before {
    content: ""; position: absolute; left: 0; top: 4px;
    border-left: 8px solid var(--ink-light);
    border-top: 4.5px solid transparent;
    border-bottom: 4.5px solid transparent;
  }
  .band__title { font-weight: 700; font-size: 16px; letter-spacing: .3px; }
  .band__text { font-size: 16px; font-weight: 400; margin-top: 2px; }
  .band__title--caps { text-transform: uppercase; font-size: 17px; }
  .brand {
    position: absolute; left: 20px; top: 92px; width: 260px;
    display: flex; align-items: center; justify-content: center; gap: 10px;
  }
  .brand__mark {
    width: 14px; height: 14px; background: var(--ink-light); flex: none;
  }
  .brand__name {
    color: var(--ink-light); font-weight: 700; font-size: 24px;
    letter-spacing: .5px; white-space: nowrap;
  }
  .divider {
    position: absolute; left: 300px; top: 26px; width: 1px; height: 166px;
    background: var(--rule);
  }
  .contact {
    position: absolute; left: 322px; top: 30px;
    color: var(--ink-light); font-size: 13px; line-height: 18px;
  }
  .contact__name { font-size: 20px; font-weight: 700; letter-spacing: .5px; margin-bottom: 4px; }
  .contact__line { display: flex; align-items: center; gap: 7px; }
  .contact__line svg { width: 11px; height: 11px; fill: var(--ink-light); flex: none; }
</style>
</head>
<body>

<section class="card card--back">
  <div class="card__dark">
    <ul class="services services--left">
      <li>Antique Repair And Restoration</li>
      <li>Art Cleaning And Remounting</li>
      <li>Art And Mirror Frame Repair</li>
      <li>Chandelier Cleaning And Restoration</li>
      <li>Document Restoration</li>
      <li>Glass, Ceramic, And Mirror Repair</li>
      <li>Hardware Repair And Restoration</li>
      <li>Kitchen Removal And Reinstallation</li>
      <li>Lamp Cleaning And Restoration</li>
      <li>Lamp Shade Replacement</li>
    </ul>
    <ul class="services services--right">
      <li>Metal Polishing And Restoration</li>
      <li>Odor Removal And Ozone Services</li>
      <li>Photo Restoration</li>
      <li>Upholstery Cleaning And Deodorizing</li>
      <li>In-house Upholstery And Reupholstery</li>
      <li>Rug Cleaning And Restoration</li>
      <li>Musical Instrument Restoration</li>
      <li>Window Treatment Repair/ Restoration</li>
      <li>Leather Restoration And Replacement</li>
      <li>Piano Restoration And Repair</li>
    </ul>
  </div>
  <div class="card__band">
    <p class="band__title">On-site Inspections And Desk Review Services</p>
    <p class="band__text">Assessment Reports And Estimates For Repair And Restoration</p>
  </div>
</section>

<section class="card card--front">
  <div class="card__dark">
    <div class="brand">
      <span class="brand__mark"></span>
      <span class="brand__name">Hallbrook Studio</span>
    </div>
    <div class="divider"></div>
    <div class="contact">
      <p class="contact__name">DANIEL MORETTI</p>
      <p>128 BROOKSIDE AVE.</p>
      <p>RIVERTON, NY 10590</p>
      <p class="contact__line">
        <svg viewBox="0 0 12 12" aria-hidden="true"><path d="M3 0h6a1 1 0 0 1 1 1v10a1 1 0 0 1-1 1H3a1 1 0 0 1-1-1V1a1 1 0 0 1 1-1zm0 1.5v8h6v-8z"/></svg>
        555.210.4832
      </p>
      <p class="contact__line">
        <svg viewBox="0 0 12 12" aria-hidden="true"><path d="M2.4 0.6l2 2.4-1.2 1.4a7 7 0 0 0 4.4 4.4l1.4-1.2 2.4 2-1.6 2A10 10 0 0 1 0.4 2.2z"/></svg>
        555.318.2700
      </p>
      <p class="contact__line">
        <svg viewBox="0 0 12 12" aria-hidden="true"><path d="M3 0h6v3H3zM1 4h10a1 1 0 0 1 1 1v5H9v2H3v-2H0V5a1 1 0 0 1 1-1zm3 4v3h4V8z"/></svg>
        555.318.2740
      </p>
      <p class="contact__line">
        <svg viewBox="0 0 12 12" aria-hidden="true"><path d="M0 2h12v1L6 7 0 3zM0 4.5l6 4 6-4V10H0z"/></svg>
        INFO@HALLBROOKSTUDIO.COM
      </p>
    </div>
  </div>
  <div class="card__band">
    <p class="band__title band__title--caps">Home Contents Restoration</p>
    <p class="band__text">Serving The General Public and The Insurance Industry for Over 40 Years</p>
  </div>
</section>

</body>
</html>
```